Lead Sales Portal Needs to Generate B2B Signup's

We are looking for banner ad designs to drive new business (B2B) traffic to our insurance and mortgage industry self serve lead sites. The sites are HomeLoanProspectHub.com and PolicyBuyerHub.com, and we service over 45,000 insurance agents and mortgage lenders in a self serve lead portal model. We want our banners to generate more of these clients.

Our clients come to our sites, browse our database and then pick out and purchase the consumer leads that they need to generate new business.

We advertise extensively on Zyntrix and on other PPC platforms, and our existing banners are looking really tired.

Some of the ad copy that works well for us is:

Cherry Pick Your Life Leads - Why Pay More Than $3.50 For Life Insurance Leads?
Sign up today and we'll match up to $250

Agents - Here's $250 For New Clients. Cherry Pick Your Life Insurance Leads & Save! Sign up today and we'll match up to $250

One of our Landing Pages that performs well is here:
http://www.policybuyerhub.com/lp/008/

One of our competitors ad's are here:

http://www.brellow.com/search/results?q=QuoteMarten&ad=427360

We're looking for a design that is eye catching, uses our "Deeply Discounted Leads" and our "$250 match bonus"

This is the second contest that we have for the same sites. The previous designs were great and really performed well, so we are looking for new designs now that 6 months have passed. I have uploaded some winning banners from the last group for your information.

Reason: I've been asked by some of the designers to delay a day to get their designs in. I'm happy to do it!

Target Market(s)

These are insurance agents and mortgage lenders. All of our clients are business' or individuals within the business. This is a B2B campaign, so we need something that is professional and upscale. These are NOT consumer facing ad's!

Industry/Entity Type

Insurance

Font styles to use
Sans Serif

Requirements
Must have
• We must have the logos for the sites in the banners. Also, we must have a call to action arrow and "Go" button. Some animation is necessary, (especially around the arrow and the GO button).

One or two designs.

File type

.JPEG
.JPG
.PNG
.GIF

File size

150 KB or smaller

Image sizes

Vertical rectangle: 240 x 400
Mobile leaderboard: 320 x 50
Banner: 468 x 60
Leaderboard: 728 x 90
Square: 250 x 250
Small square: 200 x 200
Large rectangle: 336 x 280
Inline rectangle: 300 x 250
Skyscraper: 120 x 600
Wide skyscraper: 160 x 600
Half-page: 300 x 600
Large leaderboard: 970 x 90

```html
<!DOCTYPE html>
<html lang="en">
<head>
<meta charset="utf-8">
<title>Policy Buyer Hub – Banner Set</title>
<link rel="stylesheet" href="https://fonts.googleapis.com/css2?family=Arimo:wght@700&family=Open+Sans:wght@400&family=Roboto+Condensed:wght@400;700&display=swap">
<style>
  :root{
    --backdrop-1:#6a3418;
    --backdrop-2:#4a200c;
    --header:#2c2c2c;
    --green:#7fb21f;
    --green-dark:#4f7d0e;
    --photo-1:#f2f6f8;
    --photo-2:#c9d6de;
    --beige:#cdbfa9;
    --panel-1:#e6e6e6;
    --panel-2:#c4c4c4;
    --headline:#2f2f2f;
    --list-bg:#262626;
    --cta-1:#8e8e8e;
    --cta-2:#666;
    --white:#fff;
    --button-1:#4a4a4a;
    --button-2:#1c1c1c;
  }
  *{margin:0;padding:0;box-sizing:border-box}
  html,body{width:1200px;height:1000px;overflow:hidden}
  body{background:linear-gradient(100deg,var(--backdrop-1),var(--backdrop-2) 45%,var(--backdrop-1) 75%,var(--backdrop-2));}
  .stage{position:absolute;left:0;top:0;width:941px;height:784px;transform:scale(1.2753);transform-origin:0 0}

  .banner{position:absolute;overflow:hidden;background:var(--list-bg);font-family:"Roboto Condensed",sans-serif;box-shadow:0 3px 10px rgba(0,0,0,.35)}
  .banner > *{position:absolute}
  .header{left:0;top:0;width:100%;background:var(--header)}
  .swoosh{left:0;width:100%}
  .logo{display:flex;align-items:center;gap:6px;left:0;width:100%;justify-content:center;color:var(--white);font-family:"Open Sans",sans-serif;font-weight:400;white-space:nowrap}
  .logo-dot{border-radius:50%;background:var(--white);flex:none}
  .photo{background:radial-gradient(ellipse at 40% 35%,var(--photo-1),var(--photo-2))}
  .beige-curve{left:0;width:100%}
  .headline-panel{left:0;width:100%;background:linear-gradient(var(--panel-1),var(--panel-2))}
  .headline{color:var(--headline);font-weight:700;text-transform:uppercase;text-align:center;line-height:1.3}
  .green-rule{left:0;width:100%;background:var(--green)}
  .perks{list-style:none;color:var(--white)}
  .perks li{display:flex;align-items:center}
  .perks li::before{content:"";flex:none;border-radius:50%;background:var(--white);box-shadow:inset 0 0 0 2px var(--white),inset 0 0 0 4px var(--list-bg)}
  .cta{left:0;width:100%;background:linear-gradient(var(--cta-1),var(--cta-2))}
  .cta-text{color:var(--white);line-height:1.22}
  .cta-text strong{font-weight:700}
  .go{display:flex;align-items:center;justify-content:space-between;border-radius:9px;background:linear-gradient(var(--button-1),var(--button-2));border:1px solid #777;color:var(--white);font-family:"Arimo",sans-serif;font-weight:700}
  .go svg{display:block}
  .cue{overflow:visible}

  /* Half-page 300x600 */
  .half-page{left:23px;top:48px;width:300px;height:600px}
  .half-page .header{height:72px}
  .half-page .logo{top:12px;font-size:19px}
  .half-page .logo-dot{width:30px;height:30px}
  .half-page .swoosh{top:52px;height:40px}
  .half-page .photo{left:0;top:82px;width:300px;height:230px}
  .half-page .beige-curve{top:280px;height:40px}
  .half-page .headline-panel{top:312px;height:92px}
  .half-page .headline{left:0;width:100%;top:324px;font-size:23px}
  .half-page .green-rule{top:402px;height:4px}
  .half-page .perks{left:32px;top:419px;font-size:20.5px}
  .half-page .perks li{height:26px;gap:10px}
  .half-page .perks li::before{width:11px;height:11px}
  .half-page .cta{top:512px;height:88px}
  .half-page .cta-text{left:13px;top:527px;font-size:20.5px}
  .half-page .cta-text strong{font-size:25px}
  .half-page .go{left:210px;top:560px;width:80px;height:32px;padding:0 6px 0 12px;font-size:17px}
  .half-page .cue{left:230px;top:532px}

  /* Vertical rectangle 240x400 */
  .vertical{left:354px;top:248px;width:240px;height:400px}
  .vertical .header{height:50px}
  .vertical .logo{top:9px;font-size:18px}
  .vertical .logo-dot{width:28px;height:28px}
  .vertical .swoosh{top:36px;height:30px}
  .vertical .photo{left:0;top:62px;width:240px;height:150px}
  .vertical .beige-curve{top:190px;height:30px}
  .vertical .headline-panel{top:214px;height:60px}
  .vertical .headline{left:0;width:100%;top:224px;font-size:15px}
  .vertical .green-rule{top:273px;height:3px}
  .vertical .perks{left:30px;top:278px;font-size:14px}
  .vertical .perks li{height:19px;gap:8px}
  .vertical .perks li::before{width:8px;height:8px}
  .vertical .cta{top:340px;height:60px}
  .vertical .cta-text{left:12px;top:347px;font-size:16.5px}
  .vertical .cta-text strong{font-size:20px}
  .vertical .go{left:167px;top:368px;width:66px;height:26px;padding:0 4px 0 10px;font-size:14px}
  .vertical .cue{left:180px;top:346px}

  /* Square 250x250 */
  .square{left:650px;top:398px;width:250px;height:250px;background:var(--photo-1)}
  .square .header{height:36px}
  .square .logo{top:6px;font-size:15px}
  .square .logo-dot{width:22px;height:22px}
  .square .swoosh{top:26px;height:24px}
  .square .photo{left:0;top:44px;width:112px;height:112px}
  .square .headline-panel{top:0;height:0}
  .square .headline{left:112px;width:134px;top:70px;font-size:12.5px;line-height:1.45}
  .square .beige-curve{top:140px;height:24px}
  .square .list-panel{left:0;top:156px;width:250px;height:54px;background:linear-gradient(var(--panel-1),var(--panel-2))}
  .square .perks{left:52px;top:158px;font-size:11.5px;color:var(--headline);font-weight:700}
  .square .perks li{height:16px;gap:6px}
  .square .perks li::before{width:7px;height:7px;background:var(--headline);box-shadow:inset 0 0 0 1px var(--headline),inset 0 0 0 2px var(--panel-1)}
  .square .cta{top:210px;height:40px;background:var(--list-bg)}
  .square .cta-text{left:0;width:170px;text-align:center;top:212px;font-size:14px;line-height:1.1}
  .square .cta-text strong{font-size:15px}
  .square .go{left:185px;top:222px;width:56px;height:22px;padding:0 3px 0 8px;font-size:12px}
  .square .cue{left:160px;top:210px}

  .size-label{position:absolute;top:678px;width:300px;text-align:center;color:var(--white);font-family:"Arimo",sans-serif;font-weight:700;font-size:46px;letter-spacing:-0.5px}
</style>
</head>
<body>
<main class="stage">

  <section class="banner half-page" aria-label="Half-page banner">
    <div class="photo" role="img" aria-label="Photo of two young business professionals in light blue shirts in a bright office"></div>
    <div class="header"></div>
    <svg class="swoosh" viewBox="0 0 300 40" preserveAspectRatio="none"><path d="M0 22 Q150 -4 300 6 L300 0 L0 0Z" fill="var(--header)"/><path d="M0 22 Q150 -4 300 6 L300 14 Q150 6 0 38Z" fill="var(--green)"/></svg>
    <div class="logo"><span class="logo-dot"></span>Policy Buyer Hub</div>
    <svg class="beige-curve" viewBox="0 0 300 40" preserveAspectRatio="none"><path d="M0 40 Q150 0 300 20 L300 40Z" fill="var(--beige)"/></svg>
    <div class="headline-panel"></div>
    <h2 class="headline">Why pay more than $3.50<br>for life insurance leads?</h2>
    <div class="green-rule"></div>
    <ul class="perks"><li>Chery Pick Your Leads</li><li>No Minimums</li><li>Deeply Discounted Leads</li></ul>
    <div class="cta"></div>
    <p class="cta-text">Sign up today and we'll<br>match up to <strong>$250</strong></p>
    <svg class="cue" width="50" height="26"><path d="M0 4 Q34 0 46 20" stroke="var(--white)" stroke-width="2" fill="none"/><path d="M40 19 L47 23 L48 14" stroke="var(--white)" stroke-width="2" fill="none"/></svg>
    <a class="go">GO<svg width="24" height="22" viewBox="0 0 24 22"><path d="M2 7h10V1l11 10-11 10v-6H2z" fill="var(--green)" stroke="var(--green-dark)"/></svg></a>
  </section>

  <section class="banner vertical" aria-label="Vertical rectangle banner">
    <div class="photo" role="img" aria-label="Photo of two young business professionals in light blue shirts in a bright office"></div>
    <div class="header"></div>
    <svg class="swoosh" viewBox="0 0 300 40" preserveAspectRatio="none"><path d="M0 22 Q150 -4 300 6 L300 0 L0 0Z" fill="var(--header)"/><path d="M0 22 Q150 -4 300 6 L300 14 Q150 6 0 38Z" fill="var(--green)"/></svg>
    <div class="logo"><span class="logo-dot"></span>Policy Buyer Hub</div>
    <svg class="beige-curve" viewBox="0 0 300 40" preserveAspectRatio="none"><path d="M0 40 Q150 0 300 20 L300 40Z" fill="var(--beige)"/></svg>
    <div class="headline-panel"></div>
    <h2 class="headline">Why pay more than $3.50<br>for life insurance leads?</h2>
    <div class="green-rule"></div>
    <ul class="perks"><li>Chery Pick Your Leads</li><li>No Minimums</li><li>Deeply Discounted Leads</li></ul>
    <div class="cta"></div>
    <p class="cta-text">Sign up today and we'll<br>match up to <strong>$250</strong></p>
    <svg class="cue" width="40" height="20"><path d="M0 3 Q26 0 36 15" stroke="var(--white)" stroke-width="1.5" fill="none"/><path d="M31 14 L37 17 L37 10" stroke="var(--white)" stroke-width="1.5" fill="none"/></svg>
    <a class="go">GO<svg width="20" height="18" viewBox="0 0 24 22"><path d="M2 7h10V1l11 10-11 10v-6H2z" fill="var(--green)" stroke="var(--green-dark)"/></svg></a>
  </section>

  <section class="banner square" aria-label="Square banner">
    <div class="photo" role="img" aria-label="Photo of two young business professionals in light blue shirts"></div>
    <div class="header"></div>
    <svg class="swoosh" viewBox="0 0 300 40" preserveAspectRatio="none"><path d="M0 22 Q150 -4 300 6 L300 0 L0 0Z" fill="var(--header)"/><path d="M0 22 Q150 -4 300 6 L300 14 Q150 6 0 38Z" fill="var(--green)"/></svg>
    <div class="logo"><span class="logo-dot"></span>Policy Buyer Hub</div>
    <h2 class="headline">Why pay more than<br>$3.50 for life<br>insurance leads?</h2>
    <svg class="beige-curve" viewBox="0 0 300 40" preserveAspectRatio="none"><path d="M0 40 Q150 0 300 20 L300 40Z" fill="var(--beige)"/></svg>
    <div class="list-panel"></div>
    <ul class="perks"><li>Chery Pick Your Leads</li><li>No Minimums</li><li>Deeply Discounted Leads</li></ul>
    <div class="cta"></div>
    <p class="cta-text">Sign up today and we'll<br>match up to <strong>$250</strong></p>
    <svg class="cue" width="30" height="14"><path d="M0 2 Q20 0 27 10" stroke="var(--white)" stroke-width="1.2" fill="none"/><path d="M23 9 L28 12 L28 6" stroke="var(--white)" stroke-width="1.2" fill="none"/></svg>
    <a class="go">GO<svg width="16" height="15" viewBox="0 0 24 22"><path d="M2 7h10V1l11 10-11 10v-6H2z" fill="var(--green)" stroke="var(--green-dark)"/></svg></a>
  </section>

  <p class="size-label" style="left:23px">300 x 600</p>
  <p class="size-label" style="left:324px">240 x 400</p>
  <p class="size-label" style="left:625px">250 x 250</p>

</main>
</body>
</html>
```